Political Marketing Company needs Valentine's Day card - Wall

We need a 5"x7" Valentine's Day card in the style of the attached images. We want it to be slightly cartoon-y, but heartfelt. Copy for card is as follows, with creative direction in parenthesis - line breaks are indicated by forward slash: Outside: You know I love walls… (graphic of border wall - bold, san serif font interacting with the wall in some way)Inside: But you tore down / the one around my heart! Happy Valentine’s Day! (Photo of heart with fence fallen down around it - same font as outside)

Sans Serif

```html
<!DOCTYPE html>
<html lang="en">
<head>
<meta charset="utf-8">
<title>Valentine's Day Card – Walls</title>
<link rel="stylesheet" href="https://fonts.googleapis.com/css2?family=Open+Sans:wght@700;800&display=swap">
<style>
  :root {
    --backdrop: #f8e4c0;
    --gold: #e8b92a;
    --gold-deep: #b8860b;
    --bronze: #9a6a1a;
    --heart-light: #fffaf0;
    --heart-warm: #f6cf8c;
    --ink-brown: #a8691c;
    --ink-red: #c0141a;
    --rose-grey-light: #b5b5b5;
    --rose-grey-dark: #6e6e6e;
    --rose-red: #d4170f;
    --rose-dark: #3a0503;
  }
  * { box-sizing: border-box; margin: 0; padding: 0; }
  html, body {
    width: 1200px; height: 696px; overflow: hidden;
    background: var(--backdrop);
    font-family: "Open Sans", Arial, sans-serif;
  }
  .canvas { position: relative; width: 1200px; height: 696px; }

  .card {
    position: absolute; top: 150px;
    width: 540px; height: 386px;
    border: 6px solid var(--gold);
    overflow: hidden;
  }
  .card--inside { left: 40px; }
  .card--outside { left: 620px; border-color: var(--bronze); }

  .card__roses { position: absolute; inset: 0; }
  .card--inside .card__roses {
    background: radial-gradient(circle at 30% 30%, var(--rose-grey-light), var(--rose-grey-dark) 70%, #4e4e4e);
  }
  .card--outside .card__roses {
    background: radial-gradient(circle at 40% 40%, var(--rose-red), #a30e0a 55%, var(--rose-dark));
  }

  .card__heart {
    position: absolute; left: 50%; top: 50%;
    width: 420px; height: 336px;
    transform: translate(-50%, -50%);
  }

  .card__message {
    position: absolute; left: 50%; top: 50%;
    transform: translate(-50%, -50%);
    text-align: center; width: 340px;
  }
  .message__lead {
    color: var(--ink-brown); font-weight: 700;
    font-size: 21px; line-height: 1.25; margin-top: -30px;
  }
  .message__greeting {
    color: var(--ink-red); font-weight: 800;
    font-size: 28px; line-height: 1.2; margin-top: 10px;
  }
  .message__tease {
    color: var(--ink-red); font-weight: 800;
    font-size: 34px; line-height: 1.2;
  }
  .message__icon { display: block; margin: -20px auto 6px; width: 46px; height: 40px; }
</style>
</head>
<body>
<div class="canvas">

  <section class="card card--inside">
    <div class="card__roses" role="img" aria-label="Grey roses background pattern"></div>
    <svg class="card__heart" viewBox="0 0 500 400" aria-hidden="true">
      <defs>
        <linearGradient id="heart-fill-inside" x1="0" y1="0" x2="1" y2="0">
          <stop offset="0" stop-color="var(--heart-warm)"/>
          <stop offset="0.7" stop-color="var(--heart-light)"/>
          <stop offset="1" stop-color="var(--heart-light)"/>
        </linearGradient>
        <linearGradient id="heart-rim-inside" x1="0" y1="0" x2="1" y2="1">
          <stop offset="0" stop-color="var(--gold)"/>
          <stop offset="0.5" stop-color="#fff1c0"/>
          <stop offset="1" stop-color="var(--gold-deep)"/>
        </linearGradient>
      </defs>
      <path d="M250 70 C200 10 40 0 30 130 C20 260 180 340 250 392 C320 340 480 260 470 130 C460 0 300 10 250 70 Z"
            fill="url(#heart-fill-inside)" stroke="url(#heart-rim-inside)" stroke-width="14"/>
      <path d="M250 86 C205 34 58 24 48 132 C40 250 188 322 250 370 C312 322 460 250 452 132 C442 24 295 34 250 86 Z"
            fill="none" stroke="var(--gold)" stroke-width="2"/>
    </svg>
    <div class="card__message">
      <p class="message__lead">But you tore down<br>/ the one around my heart!</p>
      <p class="message__greeting">Happy<br>Valentine's Day!</p>
    </div>
  </section>

  <section class="card card--outside">
    <div class="card__roses" role="img" aria-label="Red roses background pattern"></div>
    <svg class="card__heart" viewBox="0 0 500 400" aria-hidden="true">
      <defs>
        <linearGradient id="heart-fill-outside" x1="0" y1="0" x2="1" y2="1">
          <stop offset="0" stop-color="var(--heart-light)"/>
          <stop offset="1" stop-color="var(--heart-warm)"/>
        </linearGradient>
        <linearGradient id="heart-rim-outside" x1="0" y1="0" x2="1" y2="1">
          <stop offset="0" stop-color="var(--gold-deep)"/>
          <stop offset="0.5" stop-color="#fff1c0"/>
          <stop offset="1" stop-color="var(--gold)"/>
        </linearGradient>
      </defs>
      <path d="M250 70 C200 10 40 0 30 130 C20 260 180 340 250 392 C320 340 480 260 470 130 C460 0 300 10 250 70 Z"
            fill="url(#heart-fill-outside)" stroke="url(#heart-rim-outside)" stroke-width="14"/>
      <path d="M250 86 C205 34 58 24 48 132 C40 250 188 322 250 370 C312 322 460 250 452 132 C442 24 295 34 250 86 Z"
            fill="none" stroke="var(--gold)" stroke-width="2"/>
    </svg>
    <div class="card__message">
      <svg class="message__icon" viewBox="0 0 50 44" aria-hidden="true">
        <path d="M25 10 C20 0 2 0 2 15 C2 28 18 36 25 43 C32 36 48 28 48 15 C48 0 30 0 25 10 Z" fill="var(--ink-red)"/>
      </svg>
      <p class="message__tease">You know<br>I love walls...</p>
    </div>
  </section>

</div>
</body>
</html>
```